Family needs a book design for their memoirs

The book title will be "Calloway Kin-Tales". Their story goes back to the Larkspire as they are 13th & 14th generation descendants of four (4) of the passengers. Thomas Ashgrove, Edmund Pryce, Peter Dunmore & Walter Kinsey are all ancestors to this line. Additionally, the title bears witness to the fact that there has not been a female born in 54+ years.
We would like the front cover to display the photo of the Larkspire and this family of descendants; while the back needs to display the photo of the cross (taken by Daniel Calloway at Mt. Corvana in the Dominican Republic.

Requirements
Must have
• This book is being published by "Pages of Yours". Please use their logo (attached) on the spine. The book will be an 8 X 10 with a 1/2" spine.

```html
<!DOCTYPE html>
<html lang="en">
<head>
<meta charset="utf-8">
<title>Calloway Kin-Tales — Book Cover</title>
<link href="https://fonts.googleapis.com/css2?family=Grenze+Gotisch:wght@600&family=Lora:wght@500&display=swap" rel="stylesheet">
<style>
  :root {
    --cover-red: #b2242a;
    --cover-red-dark: #8e1a1f;
    --band-cream: #efe4c2;
    --title-cream: #efe2b6;
    --spine-line: #5b1013;
    --shadow: rgba(40, 8, 8, 0.75);
  }
  * { margin: 0; padding: 0; box-sizing: border-box; }
  html, body { width: 1200px; height: 728px; overflow: hidden; background: #ffffff; }
  .book-wrap {
    position: relative;
    width: 1200px;
    height: 728px;
    background: radial-gradient(ellipse at 50% 50%, var(--cover-red) 60%, var(--cover-red-dark) 100%);
    overflow: hidden;
  }
  .cream-band {
    position: absolute;
    left: 0; right: 0;
    top: 188px; height: 370px;
    background: var(--band-cream);
  }
  .spine {
    position: absolute;
    left: 581px; top: 0;
    width: 41px; height: 728px;
    background: var(--cover-red);
    border-left: 2px solid var(--spine-line);
    border-right: 2px solid var(--spine-line);
  }
  .spine-title {
    position: absolute;
    left: 50%; top: 38px;
    transform: translateX(-50%);
    writing-mode: vertical-rl;
    font-family: "Grenze Gotisch", "Times New Roman", serif;
    font-weight: 600;
    font-size: 25px;
    letter-spacing: 0.5px;
    color: var(--title-cream);
    text-shadow: 1px 1px 2px var(--shadow);
    white-space: nowrap;
  }
  .publisher-mark {
    position: absolute;
    left: 4px; top: 658px;
    width: 29px; height: 56px;
    background: #f6f1e4;
    display: flex;
    align-items: center;
    justify-content: center;
  }
  .publisher-name {
    writing-mode: vertical-rl;
    font-family: "Lora", Georgia, serif;
    font-weight: 500;
    font-size: 6.5px;
    color: #6a5a3a;
    white-space: nowrap;
  }
  .cover-title {
    position: absolute;
    width: 560px;
    left: 625px;
    text-align: center;
    font-family: "Grenze Gotisch", "Times New Roman", serif;
    font-weight: 600;
    font-size: 96px;
    line-height: 1;
    color: var(--title-cream);
    text-shadow: 3px 4px 4px var(--shadow);
    white-space: nowrap;
  }
  .cover-title--top { top: 46px; }
  .cover-title--bottom { top: 588px; }
  .photo-frame {
    position: absolute;
    filter: drop-shadow(3px 4px 4px rgba(60, 30, 10, 0.55));
  }
  .photo-frame--back { left: 78px; top: 218px; width: 440px; height: 324px; }
  .photo-frame--front { left: 652px; top: 196px; width: 512px; height: 336px; }
</style>
</head>
<body>
<div class="book-wrap">
  <div class="cream-band"></div>

  <!-- back cover photo -->
  <svg class="photo-frame photo-frame--back" viewBox="0 0 440 324" role="img" aria-label="Photograph of the cross statue silhouetted against a sunlit blue sky with clouds at Mt. Corvana">
    <defs>
      <linearGradient id="backSky" x1="0" y1="0" x2="1" y2="1">
        <stop offset="0" stop-color="#2f4670"/>
        <stop offset="0.45" stop-color="#4a6190"/>
        <stop offset="1" stop-color="#c9d2df"/>
      </linearGradient>
    </defs>
    <polygon fill="url(#backSky)" points="6,10 60,6 120,12 190,4 260,10 330,5 400,12 432,8 428,60 434,120 426,190 433,250 428,312 370,318 300,312 230,319 160,313 90,320 20,314 4,318 10,250 2,180 9,110 3,50"/>
  </svg>

  <!-- front cover photo -->
  <svg class="photo-frame photo-frame--front" viewBox="0 0 512 336" role="img" aria-label="Photograph of the family of descendants standing on the dock in front of the Larkspire ship replica in the harbour">
    <defs>
      <linearGradient id="frontHarbour" x1="0" y1="0" x2="0" y2="1">
        <stop offset="0" stop-color="#dcdde2"/>
        <stop offset="0.62" stop-color="#c8cacd"/>
        <stop offset="0.72" stop-color="#7d715e"/>
        <stop offset="1" stop-color="#8fb0a8"/>
      </linearGradient>
    </defs>
    <polygon fill="url(#frontHarbour)" points="10,8 80,12 150,4 230,10 310,6 390,12 470,5 506,10 500,70 508,140 501,210 507,280 502,330 430,326 350,332 270,325 190,331 110,326 40,332 6,328 12,260 4,190 11,120 5,60"/>
  </svg>

  <div class="spine">
    <div class="spine-title">Calloway Kin-Tales</div>
    <div class="publisher-mark"><span class="publisher-name">Pages of Yours</span></div>
  </div>

  <h1 class="cover-title cover-title--top">Calloway</h1>
  <div class="cover-title cover-title--bottom">Kin-Tales</div>
</div>
</body>
</html>
```